Option Sheet

We need a one page option sheet with a left to right reading of the five options. It should be a one sheet, multiple colors and definitive separations between options This is used in a sales consultation. Backround or colors not in option need to have the follow RGB value (5 red, 20 green, 63 blue)

We added a smaller text file, please change that point

Target Market(s)

Divorce

Industry/Entity Type

Legal

Requirements
Must have
• 1) All five options left to right
• 2)language included in sheet

```html
<!DOCTYPE html>
<html lang="en">
<head>
<meta charset="utf-8">
<title>Five Option Divorce Sheet</title>
<link href="https://fonts.googleapis.com/css2?family=Montserrat:wght@300;400;500;600&display=swap" rel="stylesheet">
<style>
  :root {
    --navy: rgb(5, 20, 63);
    --white: #ffffff;
    --beam: #3f4a8a;
    --gold: #d9a83c;
    --text: #e8eaf2;
    --violet: #d98ae8;
    --lime: #e4f06a;
    --coral: #f07a63;
    --pale-yellow: #f1f08a;
    --green: #5fe07a;
  }
  * { box-sizing: border-box; margin: 0; padding: 0; }
  html, body { width: 1200px; height: 1000px; overflow: hidden; background: var(--white); }
  body { font-family: "Montserrat", Arial, sans-serif; position: relative; }
  .stage { position: absolute; left: 0; top: 0; width: 1165px; height: 960px; transform: scale(1.03); transform-origin: 0 0; }
  .sheet-label { position: absolute; left: 51px; top: 34px; font-size: 42px; font-weight: 400; color: #000; }
  .title-band { position: absolute; left: 51px; top: 109px; width: 1064px; height: 96px; background: var(--navy); display: flex; align-items: center; justify-content: center; }
  .title-band h1 { font-weight: 400; font-size: 36px; letter-spacing: 1.2px; color: var(--white); }
  .options-panel { position: absolute; left: 51px; top: 211px; width: 1064px; height: 651px; background: var(--navy); }
  .frame { position: absolute; left: 0; top: 0; width: 1165px; height: 960px; pointer-events: none; }
  .icon-ring { position: absolute; width: 116px; height: 116px; border: 1px solid var(--white); border-radius: 50%; display: flex; align-items: center; justify-content: center; background: var(--navy); }
  .icon-art { width: 66px; height: 66px; border-radius: 50%; }
  .option-name { position: absolute; width: 220px; text-align: center; font-size: 12.5px; font-weight: 500; color: var(--white); }
  .option-card { position: absolute; font-size: 9.6px; line-height: 15.6px; font-weight: 400; color: var(--text); }
  .option-card h3 { font-size: 11.5px; font-weight: 400; color: var(--gold); margin-bottom: 14px; }
  .option-card h3.cons { margin: 6px 0 13px; }
  .option-card ul { list-style: none; }
  .option-card li { padding-left: 5px; text-indent: -5px; }
  .option-card li::before { content: "· "; }
</style>
</head>
<body>
<div class="stage">
  <div class="sheet-label">Option 1</div>
  <header class="title-band"><h1>FIVE OPTION DIVORCE SHEET</h1></header>
  <section class="options-panel"></section>

  <svg class="frame" viewBox="0 0 1165 960" aria-hidden="true">
    <g fill="var(--beam)">
      <polygon points="118,340 198,340 175,402 141,402"/>
      <polygon points="321,340 401,340 378,402 344,402"/>
      <polygon points="518,340 598,340 575,402 541,402"/>
      <polygon points="696,340 776,340 753,402 719,402"/>
      <polygon points="917,340 997,340 974,402 940,402"/>
    </g>
    <g fill="var(--beam)">
      <polygon points="152,423 164,423 158,434"/>
      <polygon points="355,423 367,423 361,434"/>
      <polygon points="553,424 565,424 559,435"/>
      <polygon points="733,421 745,421 739,432"/>
      <polygon points="944,423 956,423 950,434"/>
    </g>
    <g fill="none" stroke="var(--white)" stroke-width="5" stroke-linecap="round" stroke-linejoin="round">
      <path d="M240,538 V466 Q240,436 210,436 H125 Q95,436 95,466 V798 Q95,828 125,828 H210 Q240,828 240,798 V705 L292,545 V466 Q292,436 322,436 H405 Q435,436 435,466 V538"/>
      <path d="M292,725 V798 Q292,828 322,828 H405 Q435,828 435,798 V705 L489,545 V466 Q489,436 519,436 H602 Q632,436 632,466 V540"/>
      <path d="M489,725 V798 Q489,828 519,828 H602 Q632,828 632,798 V705 L665,545 V463 Q665,433 695,433 H788 Q818,433 818,463 V530"/>
      <path d="M665,700 V796 Q665,826 695,826 H788 Q818,826 818,796 V700 L884,545 V463 Q884,433 914,433 H1000 Q1030,433 1030,463 V530"/>
      <path d="M884,730 V798 Q884,828 914,828 H1000 Q1030,828 1030,798 V712 L1055,628"/>
    </g>
    <g fill="var(--white)">
      <ellipse cx="240" cy="543" rx="8" ry="11"/>
      <ellipse cx="435" cy="545" rx="8" ry="11"/>
      <ellipse cx="818" cy="537" rx="8" ry="11"/>
      <ellipse cx="1030" cy="537" rx="8" ry="11"/>
      <ellipse cx="292" cy="717" rx="8" ry="11"/>
      <ellipse cx="489" cy="717" rx="8" ry="11"/>
    </g>
  </svg>

  <div class="icon-ring" style="left:100px;top:237px"><span class="icon-art" role="img" aria-label="Icon: person relaxing in a rocking chair" style="background:var(--violet)"></span></div>
  <div class="icon-ring" style="left:303px;top:237px"><span class="icon-art" role="img" aria-label="Icon: two people talking across a desk" style="background:var(--lime)"></span></div>
  <div class="icon-ring" style="left:500px;top:237px"><span class="icon-art" role="img" aria-label="Icon: person hurrying with tools and paperwork" style="background:var(--coral)"></span></div>
  <div class="icon-ring" style="left:678px;top:237px"><span class="icon-art" role="img" aria-label="Icon: hands holding a legal document" style="background:var(--pale-yellow)"></span></div>
  <div class="icon-ring" style="left:899px;top:237px"><span class="icon-art" role="img" aria-label="Icon: attorney with a check mark" style="background:var(--green)"></span></div>

  <div class="option-name" style="left:48px;top:403px">DO NOTHING</div>
  <div class="option-name" style="left:251px;top:403px">GO TO COUNSELING</div>
  <div class="option-name" style="left:449px;top:405px">DO IT YOURSELF</div>
  <div class="option-name" style="left:629px;top:403px">LIMITED REPRESENTATION</div>
  <div class="option-name" style="left:840px;top:405px">HIRE US</div>

  <article class="option-card" style="left:113px;top:463px;width:120px">
    <h3>Advantages:</h3>
    <ul><li>Stay married</li><li>No life Changes</li></ul>
    <h3 class="cons">Disadvantages:</h3>
    <ul style="line-height:12px"><li>Remain unhappy, depressed, anxious</li><li>Money and assets may disappear</li><li>What is going to change?</li></ul>
  </article>

  <article class="option-card" style="left:304px;top:463px;width:128px">
    <h3>Advantages:</h3>
    <ul><li>Reconcile marriage</li><li>Help make a better life</li></ul>
    <h3 class="cons" style="margin-top:16px">Disadvantages:</h3>
    <ul><li>Past issues are highlighted and may drudge up old wounds.</li><li>It may just clarify the reasons you need to separate and/or divorce.</li><li>Both parties must be invested and willing to participate.</li></ul>
  </article>

  <article class="option-card" style="left:499px;top:463px;width:124px">
    <h3>Advantages:</h3>
    <ul><li>No attorney fees</li><li>You are your on attorney</li></ul>
    <h3 class="cons" style="margin-top:16px">Disadvantages:</h3>
    <ul><li>People often find that what is “fair,” may in fact, not be truly fair.</li><li>Often times, people do not know the risks.</li><li>Complicated legal system within intrigue rules</li><li>Unsure how to complete the necessary paperwork and meet the deadlines</li></ul>
  </article>

  <article class="option-card" style="left:678px;top:458px;width:128px">
    <h3 style="margin-bottom:6px">Advantages:</h3>
    <ul><li>Balance between going alone and our limited involvement in the case</li></ul>
    <h3 class="cons" style="margin:3px 0 5px">Disadvantages:</h3>
    <ul><li>Our terms may not benefit from our legal knowledge</li><li>The legal consequences of your legal documents will not be explained to you so that you can formulate a plan for handling the rest of your case.</li><li>Your spouse or other parties may cause your legal fees to increase significantly without action on your part</li></ul>
  </article>

  <article class="option-card" style="left:890px;top:463px;width:126px">
    <h3>Advantages:</h3>
    <ul><li>Gain the full benefits of our experience</li><li>Have a team of Family Law focus attorneys</li><li>Often saves you or makes you money in the long run</li><li>Save you time, energy and stress</li></ul>
    <h3 class="cons" style="margin-top:14px">Disadvantages:</h3>
    <ul><li>Initial cost</li></ul>
  </article>
</div>
</body>
</html>
```